CareStatute Chambers Mailer for Small Medical Offices and Solo Physician Practices

CareStatute Chambers -- We are a local health law firm looking to provide advice to medical practices on the legal issues they face. We strive to function as a general counsel for medical practices and provide tailored solutions to meet the needs of our clients. Please see postcard content ideas in document attached. Our firm colors are royal blue, gray and white and black.

Target Market(s)

Small medical offices, solo physician practices in the Southeast Michigan (Detroit Metro area)

Industry/Entity Type

Law Firm

Font styles to use
Sans Serif

Colors
0991cd
3176b5
ffffff
7f7f7f
1b1b1b

Requirements
Must have
• Brief summary of legal services offered, bullet pointed list of practice areas/issues
• Contact information, website, address
• Pictures of attorneys
• Prefer the use of our firm's colors (royal blue, gray, white, black)
Nice to have
• Included some purchased stock images that could also be incorporated

```html
<!DOCTYPE html>
<html lang="en">
<head>
<meta charset="utf-8">
<title>CareStatute Chambers – Postcard Mailer</title>
<link href="https://fonts.googleapis.com/css2?family=Oswald:wght@600&family=Questrial&family=Arimo:ital,wght@0,400;0,700;1,700&display=swap" rel="stylesheet">
<style>
  :root {
    --royal: #0d67b5;
    --headline-blue: #1f6fb6;
    --gray: #7f7f7f;
    --gray-band: #8a8a8a;
    --bubble-dark: #8c8c8c;
    --bubble-light: #a3a3a3;
    --ink: #1b1b1b;
    --white: #ffffff;
    --paper-light: #f4f5f7;
    --paper-mid: #e3e6ea;
  }
  * { box-sizing: border-box; margin: 0; padding: 0; }
  html, body {
    width: 1061px; height: 1200px; overflow: hidden;
    background: var(--white);
    font-family: "Questrial", "Century Gothic", sans-serif;
    color: var(--ink);
  }
  .canvas { position: relative; width: 1061px; height: 1200px; }
  .card {
    position: absolute; left: 50px; width: 960px; height: 534px;
    overflow: hidden;
    background: linear-gradient(135deg, var(--paper-light) 0%, var(--paper-mid) 45%, var(--paper-light) 70%, var(--paper-mid) 100%);
    border: 1px solid #d5d9de;
  }
  .card--front { top: 40px; }
  .card--back { top: 622px; }
  .abs { position: absolute; }

  /* Front */
  .front-panel { position: absolute; inset: 0; }
  .headline {
    left: 42px; top: 72px;
    font-family: "Oswald", "Arial Narrow", sans-serif; font-weight: 600;
    font-size: 33px; letter-spacing: 0.2px; line-height: 1;
    color: var(--headline-blue);
  }
  .headline .muted { color: var(--gray); }
  .visual-questions {
    left: 355px; top: 30px; width: 125px; height: 105px; border-radius: 10px;
    background: radial-gradient(circle at 55% 45%, #4a90d0 0%, #7fb2de 45%, rgba(230,235,240,0) 75%);
  }
  .visual-gavel {
    left: 40px; top: 165px; width: 500px; height: 320px; border-radius: 20px;
    background: radial-gradient(ellipse at 50% 55%, #5b3b2f 0%, #2c4a78 35%, #b9c2cc 65%, rgba(235,238,241,0) 85%);
  }
  .brand-front {
    left: 575px; top: 25px; width: 385px; height: 78px;
    display: flex; align-items: center; justify-content: center; gap: 14px;
  }
  .brand-name {
    font-family: "Questrial", sans-serif; font-size: 31px; color: var(--royal);
    white-space: nowrap;
  }
  .brand-mark { width: 22px; height: 22px; background: var(--gray); }
  .front-copy {
    left: 595px; top: 124px; width: 350px; text-align: center;
    color: var(--white); font-size: 18px; line-height: 24.5px;
  }
  .talk-icon { left: 722px; top: 236px; width: 96px; height: 62px; }
  .consult {
    left: 575px; top: 312px; width: 390px; text-align: center;
    font-family: "Arimo", Arial, sans-serif; font-weight: 700; color: var(--white);
    font-size: 17px; line-height: 21px;
  }
  .consult em { display: block; font-style: italic; font-size: 15px; }
  .front-phone {
    left: 575px; top: 372px; width: 390px; text-align: center;
    color: var(--white); font-size: 27px; line-height: 32px; letter-spacing: 0.5px;
  }
  .front-web, .front-mail {
    left: 575px; width: 390px; text-align: center; color: var(--white);
    font-size: 18px; line-height: 22px; letter-spacing: 1.2px;
  }
  .front-web { top: 416px; }
  .front-mail { top: 447px; font-size: 16.5px; }

  /* Back */
  .info-block { left: 27px; top: 28px; width: 472px; height: 438px; background: var(--royal); }
  .brand-back {
    left: 27px; top: 28px; width: 472px; height: 99px; background: var(--white);
    display: flex; align-items: center; justify-content: center; gap: 14px;
  }
  .brand-back .brand-name { font-size: 33px; }
  .intro {
    left: 55px; top: 142px; width: 292px;
    color: var(--white); font-size: 12.4px; line-height: 15.4px;
  }
  .services {
    left: 68px; top: 218px; list-style: none;
    color: var(--white); font-size: 12.4px; line-height: 15.2px;
  }
  .services li::before { content: "\2022"; margin-right: 4px; }
  .contact-band {
    left: 27px; top: 397px; width: 327px; height: 62px; background: var(--gray-band);
    color: var(--white); text-align: center; font-size: 18px; line-height: 22px; padding-top: 8px;
    letter-spacing: 0.3px;
  }
  .portrait {
    width: 118px; height: 118px; border: 2px solid var(--white);
    background: linear-gradient(180deg, #9aa6b2 0%, #5f6e80 60%, #2f3b4b 100%);
  }
  .portrait--one { left: 365px; top: 138px; }
  .portrait--two { left: 367px; top: 300px; background: linear-gradient(180deg, #7d6a5e 0%, #4e4a52 55%, #24283a 100%); }
  .attorney {
    width: 150px; text-align: center; color: var(--white);
    font-family: "Arimo", Arial, sans-serif; font-weight: 700; font-size: 10.5px; line-height: 13.5px;
  }
  .attorney--one { left: 349px; top: 263px; }
  .attorney--two { left: 351px; top: 424px; }
  .return-address {
    left: 586px; top: 45px; font-family: "Arimo", Arial, sans-serif; font-style: normal;
    font-size: 11.5px; line-height: 19.5px; color: #3a3a3a;
  }
  .stamp { left: 811px; top: 34px; width: 86px; height: 95px; border: 1.5px dashed #6f6f6f; }
  .address-line { left: 582px; width: 312px; border-top: 1.5px dashed #6f6f6f; }
  .address-line--1 { top: 281px; }
  .address-line--2 { top: 326px; }
  .address-line--3 { top: 372px; }
  .address-line--4 { top: 418px; }
</style>
</head>
<body>
<main class="canvas">

  <section class="card card--front" aria-label="Postcard front">
    <svg class="front-panel" width="960" height="534" viewBox="0 0 960 534" aria-hidden="true">
      <polygon points="519,0 960,0 960,534 604,534" fill="var(--royal)"/>
      <polygon points="548,25 960,25 960,103 563,103" fill="var(--white)"/>
    </svg>

    <h1 class="abs headline">HEALTH LAW <span class="muted">QUESTIONS</span></h1>
    <div class="abs visual-questions" role="img" aria-label="Blue 3D question marks"></div>
    <div class="abs visual-gavel" role="img" aria-label="Wooden gavel resting on a stethoscope"></div>

    <div class="abs brand-front">
      <span class="brand-name">CareStatute Chambers</span>
      <span class="brand-mark" aria-hidden="true"></span>
    </div>

    <p class="abs front-copy">We are local, experienced health lawyers available to provide efficient, effective advice on the issues impacting your healthcare business every day.</p>

    <svg class="abs talk-icon" viewBox="0 0 96 62" aria-hidden="true">
      <ellipse cx="30" cy="20" rx="28" ry="18" fill="var(--bubble-dark)"/>
      <polygon points="14,32 10,44 24,35" fill="var(--bubble-dark)"/>
      <ellipse cx="62" cy="38" rx="30" ry="18" fill="var(--bubble-light)"/>
      <polygon points="80,50 88,60 72,53" fill="var(--bubble-light)"/>
      <text x="30" y="25" text-anchor="middle" font-family="Questrial, sans-serif" font-size="15" fill="#fff">Let's</text>
      <text x="63" y="44" text-anchor="middle" font-family="Questrial, sans-serif" font-size="16" fill="#fff">Talk</text>
    </svg>

    <p class="abs consult">FREE CONSULTATION<em>available</em></p>
    <p class="abs front-phone">313.555.0147</p>
    <p class="abs front-web">www.carestatutechambers.com</p>
    <p class="abs front-mail">info@carestatutechambers.com</p>
  </section>

  <section class="card card--back" aria-label="Postcard back">
    <div class="abs info-block"></div>
    <div class="abs brand-back">
      <span class="brand-name">CareStatute Chambers</span>
      <span class="brand-mark" aria-hidden="true"></span>
    </div>

    <p class="abs intro">We provide personalized service to our clients so you have trusted counsel available when you need it. We offer competitive hourly rates as well as flat fee arrangements when possible.</p>

    <ul class="abs services">
      <li>Contract review and negotiation</li>
      <li>Stark and Anti-kickback matters</li>
      <li>Reimbursement and payer issues</li>
      <li>HIPAA</li>
      <li>Vendor issues</li>
      <li>Licensing matters</li>
      <li>Employee issues</li>
      <li>Difficult patient matters</li>
      <li>Subpoenas and medical record requests</li>
      <li>Leases and landlord-tenant issues</li>
    </ul>

    <div class="abs contact-band">313.555.0147<br>www.carestatutechambers.com</div>

    <div class="abs portrait portrait--one" role="img" aria-label="Portrait photo of partner Dana R. Holloway"></div>
    <p class="abs attorney attorney--one">Dana R. Holloway<br>Partner</p>
    <div class="abs portrait portrait--two" role="img" aria-label="Portrait photo of partner Marissa Kettering"></div>
    <p class="abs attorney attorney--two">Marissa Kettering<br>Partner</p>

    <address class="abs return-address">
      CareStatute Chambers<br>
      41870 Larkmoor Ave., Suite 310<br>
      Brookhaven, Michigan 48391
    </address>

    <div class="abs stamp" aria-hidden="true"></div>
    <div class="abs address-line address-line--1"></div>
    <div class="abs address-line address-line--2"></div>
    <div class="abs address-line address-line--3"></div>
    <div class="abs address-line address-line--4"></div>
  </section>

</main>
</body>
</html>
```